Alapca breeding needs a website

Presentation of the farm, animals (stallions, mares, information about the animals, for sale) and possible later expansion with a webshop (alpaca wool products). We want to present our farm and the animals on the farm on this page. A mission why we are doing this. Furthermore, each animal should be shown with a picture and described. Later we want to sell our own products made from alpaca wool via a webshop. But we still need to grow a bit to do that.

Target Market(s)

Information about my alpaca breeding and the alpaca farm

Industry/Entity Type

Tierzucht

Number of Pages Required

1 page

Font styles to use
Sans Serif

Requirements
Must have
• Modern design that matches the logo
Nice to have
• Intuitive operation / Clear structure
Should not have
• No

```html
<!DOCTYPE html>
<html lang="en">
<head>
<meta charset="utf-8">
<title>Valle Alpacas</title>
<link href="https://fonts.googleapis.com/css2?family=Lora:wght@500;600&family=Roboto:wght@400;500;700&display=swap" rel="stylesheet">
<style>
:root{
  --green:#8cc63f;
  --navy:#0f2a4a;
  --text:#3a3a3a;
  --light:#eef2f6;
  --cream:#f3f1e6;
  --white:#ffffff;
}
*{margin:0;padding:0;box-sizing:border-box}
html,body{width:1200px;height:4563px;overflow:hidden}
body{position:relative;font-family:'Roboto',sans-serif;color:var(--text);background:var(--white)}
.abs{position:absolute}
.serif{font-family:'Lora',serif;font-weight:500;color:var(--navy);text-transform:uppercase}
.btn{position:absolute;background:var(--green);color:#fff;font-size:14px;font-weight:700;text-transform:uppercase;border-radius:24px;display:flex;align-items:center;justify-content:center}
.rule{display:block;width:42px;height:4px;background:var(--green);margin-top:12px}
.body-text{font-size:15px;line-height:26px;color:#444}
.body-text p+p{margin-top:14px}

/* top bar */
.topbar{left:0;top:0;width:1200px;height:46px;background:var(--navy);color:#fff;font-size:14px}
.topbar .mail{left:110px;top:14px;display:flex;gap:10px;align-items:center}
.topbar .phone{left:768px;top:14px;display:flex;gap:10px;align-items:center}
.social{display:flex;gap:8px}
.social span{width:32px;height:32px;border:1.5px solid rgba(255,255,255,.8);border-radius:50%;display:block}
.topbar .social{position:absolute;left:938px;top:7px}

/* header */
.header{left:0;top:46px;width:1200px;height:117px;background:#fff}
.nav{left:110px;top:52px;display:flex;gap:40px;font-size:14px;font-weight:700;color:var(--navy)}
.nav .active{color:var(--green)}
.logo-disc{left:508px;top:70px;width:184px;height:160px;border-radius:0 0 92px 92px;background:#fff;z-index:3;display:flex;align-items:flex-end;justify-content:center;padding-bottom:38px}
.brand{font-family:'Lora',serif;font-weight:600;color:var(--navy);font-size:24px;letter-spacing:1px;text-align:center;line-height:1.05}
.head-contact{left:815px;top:37px;width:133px;height:46px}
.head-icons{left:980px;top:52px;display:flex;gap:22px;align-items:center;font-size:14px;color:var(--navy)}

/* hero */
.hero{left:0;top:163px;width:1200px;height:690px;background:linear-gradient(180deg,#8c9aa3 0%,#b7b6a5 28%,#7f8f4a 48%,#6c7f2e 75%,#7b8a3b 100%)}
.hero-copy{left:112px;top:350px;color:#fff}
.hero-copy .small{font-family:'Lora',serif;font-size:26px;text-transform:uppercase}
.hero-copy h1{font-family:'Lora',serif;font-weight:500;font-size:46px;text-transform:uppercase;line-height:1.1;margin-top:2px}
.hero-copy p{font-size:21px;font-weight:500;line-height:31px;margin-top:14px;width:480px}
.hero-btn{left:112px;top:529px;width:146px;height:48px}
.story-bg{left:0;top:853px;width:1200px;height:630px;background:linear-gradient(180deg,var(--cream) 0%,#e8e6d6 60%,#dcd9c3 100%)}
.dots{left:552px;top:771px;display:flex;gap:9px;z-index:2}
.dots span{width:17px;height:17px;border-radius:50%;background:#fff;display:block}
.dots span.on{background:var(--green);box-shadow:0 0 0 3px #fff inset}

/* story */
.story-mark{left:130px;top:950px;width:410px;height:380px;border-radius:50%;background:radial-gradient(circle,rgba(140,198,63,.18),rgba(15,42,74,.08));display:flex;align-items:center;justify-content:center}
.story-mark .brand{font-size:40px}
.story{left:647px;top:945px;width:443px}
.story h2{font-size:46px}
.story .body-text{margin-top:28px;text-align:justify}
.story-btn{left:647px;top:1314px;width:151px;height:47px}

/* about */
.about-head{left:0;top:1576px;width:1200px;text-align:center}
.about-head h2{font-size:42px}
.about-head .rule{margin:10px auto 0}
.about-head p{width:930px;margin:28px auto 0;font-size:15px;line-height:26px;color:#444}

.animal h2{font-size:42px}
.animal .body-text{margin-top:34px;width:465px;text-align:justify}
.photo{border-radius:50%}

/* products */
.products{left:0;top:3430px;width:1200px;height:800px;background:var(--light)}
.products-head{left:0;top:3520px;width:1200px;text-align:center}
.products-head h2{font-size:40px}
.products-head .rule{margin:10px auto 0}
.card{top:3623px;width:225px;height:282px;background:#fff;border-radius:6px;box-shadow:0 2px 10px rgba(0,0,0,.06);text-align:center}
.card.featured{border:2px solid var(--green)}
.card .thumb{width:130px;height:110px;margin:32px auto 0;border-radius:8px}
.card h3{font-size:16px;font-weight:700;color:var(--navy);margin-top:20px}
.card p{font-size:13px;line-height:21px;color:#444;margin-top:8px}
.card .price{color:var(--green);font-weight:700;font-size:14px;margin-top:6px}
.arrow{top:3747px;width:34px;height:34px;border-radius:50%}
.view-all{left:500px;top:3948px;width:200px;height:46px}

/* footer */
.footer{left:0;top:4070px;width:1200px;height:493px}
.f-brand{left:112px;top:4320px;width:175px;color:#fff}
.f-brand .brand{color:#fff;font-size:34px}
.f-col h4{font-size:17px;font-weight:700;color:#fff;text-transform:uppercase}
.f-links{left:340px;top:4228px}
.f-links li{list-style:none;color:#fff;font-size:14px;display:flex;align-items:center;gap:16px;height:45px}
.f-links li:first-child{margin-top:18px}
.f-contact{left:521px;top:4228px}
.f-contact .item{display:flex;align-items:center;gap:18px;color:#fff;font-size:14px;line-height:20px;height:50px}
.f-contact .item:first-of-type{margin-top:30px}
.f-contact .ic{width:34px;height:34px;border-radius:50%;background:#fff;display:flex;align-items:center;justify-content:center;flex:none}
.f-news{left:801px;top:4228px;width:286px}
.f-news label{display:block;color:#fff;font-size:14px;margin-top:24px;padding-bottom:10px;border-bottom:1.5px solid rgba(255,255,255,.8)}
.f-subscribe{left:801px;top:4316px;width:133px;height:48px;font-size:15px}
.f-news-social{left:801px;top:4389px}
.f-line{left:112px;top:4502px;width:975px;height:1px;background:rgba(255,255,255,.3)}
.copyright{left:0;top:4521px;width:1200px;text-align:center;color:#fff;font-size:13px}
.pay{left:907px;top:4521px;display:flex;gap:5px}
.pay span{width:32px;height:20px;border-radius:3px;background:#fff;display:block}
</style>
</head>
<body>

<!-- Top bar -->
<div class="abs topbar">
  <div class="abs mail">
    <svg width="14" height="11" viewBox="0 0 14 11"><rect width="14" height="11" rx="1.5" fill="#8cc63f"/><path d="M1 1.5l6 4.5 6-4.5" stroke="#0f2a4a" stroke-width="1.4" fill="none"/></svg>
    info@vallealpacas.com
  </div>
  <div class="abs phone">
    <svg width="13" height="13" viewBox="0 0 24 24"><path d="M6.6 10.8a15 15 0 006.6 6.6l2.2-2.2a1 1 0 011-.25 11.4 11.4 0 003.6.57 1 1 0 011 1V20a1 1 0 01-1 1A17 17 0 013 4a1 1 0 011-1h3.5a1 1 0 011 1c0 1.25.2 2.45.57 3.57a1 1 0 01-.25 1z" fill="#8cc63f"/></svg>
    +1 (555) 014 2200
  </div>
  <div class="social"><span></span><span></span><span></span><span></span></div>
</div>

<!-- Header -->
<div class="abs header">
  <nav class="abs nav"><span class="active">HOME</span><span>ABOUT US</span><span>PRODUCTS</span><span>BLOG</span></nav>
  <div class="btn head-contact">Contact Us</div>
  <div class="abs head-icons">
    <svg width="15" height="15" viewBox="0 0 24 24"><circle cx="10" cy="10" r="7" stroke="#0f2a4a" stroke-width="3" fill="none"/><path d="M15 15l7 7" stroke="#0f2a4a" stroke-width="3"/></svg>
    <svg width="14" height="15" viewBox="0 0 24 24"><circle cx="12" cy="7" r="5" fill="#0f2a4a"/><path d="M2 23c0-6 4-10 10-10s10 4 10 10z" fill="#0f2a4a"/></svg>
    <span style="display:flex;gap:4px;align-items:center"><svg width="16" height="14" viewBox="0 0 24 20"><path d="M0 1h4l3 12h13l3-9H6" stroke="#0f2a4a" stroke-width="2.6" fill="none"/><circle cx="9" cy="17.5" r="2" fill="#0f2a4a"/><circle cx="18" cy="17.5" r="2" fill="#0f2a4a"/></svg><span style="color:#8cc63f">(0)</span></span>
  </div>
</div>
<div class="abs logo-disc"><div class="brand">VALLE<br><span style="font-size:16px;letter-spacing:3px">ALPACAS</span></div></div>

<!-- Hero -->
<div class="abs hero" role="img" aria-label="Photo of a brown horse grazing in a green pasture under a cloudy sky"></div>
<div class="abs story-bg" role="img" aria-label="Faded photo of a white horse in a meadow"></div>
<svg class="abs" style="left:0;top:660px" width="1200" height="200" viewBox="0 0 1200 200">
  <path d="M0 20 Q600 340 1200 20 L1200 200 L0 200 Z" fill="#f3f1e6"/>
  <path d="M0 12 Q600 356 1200 12" stroke="#8cc63f" stroke-width="7" fill="none"/>
</svg>
<div class="abs hero-copy">
  <div class="small">Welcome to</div>
  <h1>Valle Alpacas</h1>
  <p>Lorem ipsum dolor sit amet, consectetur adipis eiusmod tempor incididuntea.</p>
</div>
<div class="btn hero-btn">Learn More</div>
<div class="abs dots"><span></span><span class="on"></span><span></span><span></span></div>

<!-- Our story -->
<div class="abs story-mark"><div class="brand">VALLE<br><span style="font-size:22px;letter-spacing:5px">ALPACAS</span></div></div>
<div class="abs story">
  <h2 class="serif">Our Story</h2>
  <span class="rule"></span>
  <div class="body-text">
    <p>Lorem ipsum dolor sit amet, consectetur adipiscing elit, sed do eiusmod tempor incididunt ut labore et dolore magna aliqua. Ut enim ad minim veniam, quis nostrud exercitation ullamco laboris nisi ut aliquip ex ea commodo consequat. Duis aute irure dolor in reprehea.</p>
    <p>Lorem ipsum dolor sit amet, consectetur adipiscing elit, sed do eiusmod tempor incididunt ut labore et dolore magna aliqua ut enim ad minim veniam, quis nostrud exercitation ullamco laboris nisi ut aliquipea.</p>
  </div>
</div>
<div class="btn story-btn">Learn More</div>

<!-- About the animals -->
<div class="abs about-head">
  <h2 class="serif">About the Animals</h2>
  <span class="rule"></span>
  <p>Lorem ipsum dolor sit amet, consectetur adipiscing elit, sed do eiusmod tempor incididunt ut labore et dolore magna aliqua. Ut enim ad minim veniam, quis nostrud exercitation ullamco laboris nisi ut aliquip ex ea commodo consequat. Duis aute irure dolor in reprehenderit in voluptate velit esse cillum dolore eu fugiat nulla pariaturea.</p>
</div>

<!-- Stallions -->
<div class="abs animal" style="left:112px;top:1805px">
  <h2 class="serif">Stallions</h2>
  <span class="rule"></span>
  <div class="body-text">
    <p>Lorem ipsum dolor sit amet, consectetur adipiscing elit, sed do eiusmod tempor incididunt ut labore et dolore magna aliqua. Ut enim ad minim veniam, quis nostrud exercitation ullamco laboris nisi ut aliquip ex ea commodo consequat. Duis aute irure dolor in repquis nostrud exercitation rehea.</p>
    <p>Lorem ipsum dolor sit amet, consectetur adipiscing elit, sed do eiusmod tempor incididunt ut labore et dolore magna aliqua ut enim ad minim veniam, quis nostrud exercitation ullamco laboris nisi ut quis nostrud exercitation aliquipea.</p>
  </div>
</div>
<div class="btn" style="left:112px;top:2173px;width:150px;height:46px">Learn More</div>
<div class="abs photo" style="left:642px;top:1798px;width:446px;height:446px;background:var(--green);padding:11px">
  <div class="photo" style="width:100%;height:100%;background:radial-gradient(circle at 50% 45%,#7a4a2a 0%,#9b7a52 35%,#c9c19a 65%,#b7c4a4 100%)" role="img" aria-label="Photo of a brown stallion standing in tall dune grass"></div>
</div>

<!-- Mares -->
<div class="abs photo" style="left:110px;top:2333px;width:446px;height:446px;background:var(--navy);padding:16px">
  <div class="photo" style="width:100%;height:100%;background:linear-gradient(180deg,#3d5a2a 0%,#5b7a35 45%,#8a5c38 60%,#6f9a3e 80%,#7aa845 100%)" role="img" aria-label="Photo of a mare and her foal grazing in a green paddock"></div>
</div>
<div class="abs animal" style="left:622px;top:2342px">
  <h2 class="serif">Mares</h2>
  <span class="rule"></span>
  <div class="body-text">
    <p>Lorem ipsum dolor sit amet, consectetur adipiscing elit, sed do eiusmod tempor incididunt ut labore et dolore magna aliqua. Ut enim ad minim veniam, quis nostrud exercitation ullamco laboris nisi ut aliquip ex ea commodo consequat. Duis aute irure dolor in repquis nostrud exercitation rehea.</p>
    <p>Lorem ipsum dolor sit amet, consectetur adipiscing elit, sed do eiusmod tempor incididunt ut labore et dolore magna aliqua ut enim ad minim veniam, quis nostrud exercitation ullamco laboris nisi ut quis nostrud exercitation aliquipea.</p>
  </div>
</div>
<div class="btn" style="left:622px;top:2710px;width:151px;height:46px">Learn More</div>

<!-- Alpaca -->
<div class="abs animal" style="left:112px;top:2879px">
  <h2 class="serif">Alpaca</h2>
  <span class="rule"></span>
  <div class="body-text">
    <p>Lorem ipsum dolor sit amet, consectetur adipiscing elit, sed do eiusmod tempor incididunt ut labore et dolore magna aliqua. Ut enim ad minim veniam, quis nostrud exercitation ullamco laboris nisi ut aliquip ex ea commodo consequat. Duis aute irure dolor in repquis nostrud exercitation rehea.</p>
    <p>Lorem ipsum dolor sit amet, consectetur adipiscing elit, sed do eiusmod tempor incididunt ut labore et dolore magna aliqua ut enim ad minim veniam, quis nostrud exercitation ullamco laboris nisi ut quis nostrud exercitation aliquipea.</p>
  </div>
</div>
<div class="btn" style="left:112px;top:3247px;width:150px;height:46px">Learn More</div>
<div class="abs photo" style="left:642px;top:2870px;width:446px;height:446px;background:var(--green);padding:11px">
  <div class="photo" style="width:100%;height:100%;background:linear-gradient(180deg,#9cc4e8 0%,#b8d3ea 35%,#e9e6de 50%,#7a9a48 70%,#6a8a3a 100%)" role="img" aria-label="Photo of a white alpaca and brown alpacas on a grassy farm"></div>
</div>

<!-- Products -->
<div class="abs products"></div>
<div class="abs products-head">
  <h2 class="serif">Alpaca Wool Products</h2>
  <span class="rule"></span>
</div>
<div class="abs card" style="left:112px">
  <div class="thumb" style="background:radial-gradient(circle,#e6e3de,#fff 70%)" role="img" aria-label="Raw white alpaca fleece"></div>
  <h3>LOREM IPSUM</h3><p>Lorem ipsum dolor sit amet,<br>consectetur adip.</p><div class="price">$19.99</div>
</div>
<div class="abs card" style="left:363px">
  <div class="thumb" style="background:linear-gradient(135deg,#c43b2e,#e0b23a 40%,#3c7bb5 70%,#fff 90%)" role="img" aria-label="Folded multicoloured woven alpaca blanket"></div>
  <h3>LOREM IPSUM</h3><p>Lorem ipsum dolor sit amet,<br>consectetur adip.</p><div class="price">$19.99</div>
</div>
<div class="abs card featured" style="left:613px">
  <div class="thumb" style="background:radial-gradient(circle,#8fbde3,#fff 72%)" role="img" aria-label="Folded light blue alpaca throw"></div>
  <h3>LOREM IPSUM</h3><p>Lorem ipsum dolor sit amet,<br>consectetur adip.</p><div class="price">$19.99</div>
</div>
<div class="abs card" style="left:863px">
  <div class="thumb" style="background:radial-gradient(circle,#ece4cf,#fff 70%)" role="img" aria-label="Ball of cream alpaca wool roving"></div>
  <h3>LOREM IPSUM</h3><p>Lorem ipsum dolor sit amet,<br>consectetur adip.</p><div class="price">$19.99</div>
</div>
<svg class="abs arrow" style="left:41px" viewBox="0 0 34 34"><circle cx="17" cy="17" r="15.5" fill="#fff" stroke="#8cc63f" stroke-width="2"/><path d="M19.5 11l-6 6 6 6" stroke="#0f2a4a" stroke-width="2.5" fill="none"/></svg>
<svg class="abs arrow" style="left:1124px" viewBox="0 0 34 34"><circle cx="17" cy="17" r="17" fill="#8cc63f"/><path d="M14.5 11l6 6-6 6" stroke="#fff" stroke-width="2.5" fill="none"/></svg>
<div class="btn view-all">View All Products</div>

<!-- Footer -->
<svg class="abs footer" viewBox="0 0 1200 493">
  <path d="M0 190 Q600 -80 1200 190 L1200 493 L0 493 Z" fill="#0f2a4a"/>
  <path d="M0 180 Q600 -96 1200 180" stroke="#8cc63f" stroke-width="7" fill="none"/>
</svg>
<div class="abs f-brand"><div class="brand">VALLE<br><span style="font-size:20px;letter-spacing:5px">ALPACAS</span></div></div>
<div class="abs f-col f-links">
  <h4>Quick Links</h4>
  <ul>
    <li><svg width="14" height="14" viewBox="0 0 14 14"><circle cx="7" cy="7" r="7" fill="#8cc63f"/><path d="M6 4l3 3-3 3" stroke="#0f2a4a" stroke-width="1.8" fill="none"/></svg>Home</li>
    <li><svg width="14" height="14" viewBox="0 0 14 14"><circle cx="7" cy="7" r="7" fill="#8cc63f"/><path d="M6 4l3 3-3 3" stroke="#0f2a4a" stroke-width="1.8" fill="none"/></svg>About Us</li>
    <li><svg width="14" height="14" viewBox="0 0 14 14"><circle cx="7" cy="7" r="7" fill="#8cc63f"/><path d="M6 4l3 3-3 3" stroke="#0f2a4a" stroke-width="1.8" fill="none"/></svg>Products</li>
    <li><svg width="14" height="14" viewBox="0 0 14 14"><circle cx="7" cy="7" r="7" fill="#8cc63f"/><path d="M6 4l3 3-3 3" stroke="#0f2a4a" stroke-width="1.8" fill="none"/></svg>Blog</li>
    <li><svg width="14" height="14" viewBox="0 0 14 14"><circle cx="7" cy="7" r="7" fill="#8cc63f"/><path d="M6 4l3 3-3 3" stroke="#0f2a4a" stroke-width="1.8" fill="none"/></svg>Contact Us</li>
  </ul>
</div>
<div class="abs f-col f-contact">
  <h4>Contact Us</h4>
  <div class="item"><span class="ic"><svg width="12" height="16" viewBox="0 0 12 16"><path d="M6 0a6 6 0 00-6 6c0 4.5 6 10 6 10s6-5.5 6-10a6 6 0 00-6-6z" fill="#8cc63f"/><circle cx="6" cy="6" r="2.2" fill="#fff"/></svg></span>123, Valle Road,<br>United States</div>
  <div class="item"><span class="ic"><svg width="14" height="11" viewBox="0 0 14 11"><rect width="14" height="11" rx="1.5" fill="#8cc63f"/><path d="M1 1.5l6 4.5 6-4.5" stroke="#fff" stroke-width="1.4" fill="none"/></svg></span>info@vallealpacas.com</div>
  <div class="item"><span class="ic"><svg width="14" height="14" viewBox="0 0 24 24"><path d="M6.6 10.8a15 15 0 006.6 6.6l2.2-2.2a1 1 0 011-.25 11.4 11.4 0 003.6.57 1 1 0 011 1V20a1 1 0 01-1 1A17 17 0 013 4a1 1 0 011-1h3.5a1 1 0 011 1c0 1.25.2 2.45.57 3.57a1 1 0 01-.25 1z" fill="#8cc63f"/></svg></span>+1 (555) 014 2200</div>
</div>
<div class="abs f-col f-news">
  <h4>Sign up to our newsletter</h4>
  <label>Email</label>
</div>
<div class="btn f-subscribe">Subscribe</div>
<div class="abs social f-news-social"><span style="width:36px;height:36px"></span><span style="width:36px;height:36px"></span><span style="width:36px;height:36px"></span><span style="width:36px;height:36px"></span></div>
<div class="abs f-line"></div>
<div class="abs copyright">© 2024 VALLE ALPACAS &nbsp;|&nbsp; All Rights Reserved</div>
<div class="abs pay"><span></span><span></span><span></span><span></span><span></span></div>

</body>
</html>
```